Bref créative
Velvet Rooms
Home Interiors
Modern
Linnea Parcot Weller
Design Consultant
412 Quillon Lane
Palm beach Gardens, Fl 33587
LinneaParcot@velmorra.example
VelvetRooms.example
My logo is the Velvet Rooms. Would like to incorporate a flur de lis.

```html
<!DOCTYPE html>
<html lang="en">
<head>
<meta charset="utf-8">
<title>Velvet Rooms Stationery</title>
<link rel="stylesheet" href="https://fonts.googleapis.com/css2?family=Cinzel:wght@400;600&family=Lato:wght@400;700&display=swap">
<style>
:root{
  --bg-top:#f4f4f4;
  --bg-bottom:#d9d9d9;
  --paper:#ffffff;
  --ink:#4a4a4a;
  --ink-soft:#8a8a8a;
  --accent:#c8102e;
  --black:#1c1c1c;
  --art:#f3c9cc;
  --art-faint:#fbe8e9;
  --shadow:0 2px 5px rgba(0,0,0,.25);
}
*{box-sizing:border-box;margin:0;padding:0}
html,body{width:1200px;height:346px;overflow:hidden}
body{background:linear-gradient(var(--bg-top),var(--bg-bottom));font-family:"Lato",sans-serif;color:var(--ink);position:relative}
.item{position:absolute;background:var(--paper);box-shadow:var(--shadow)}
.caption{position:absolute;font-size:5px;color:var(--ink-soft);text-align:center;width:100%;bottom:-10px;left:0}
.wordmark{font-family:"Cinzel",serif;font-weight:600;color:var(--ink);line-height:1;white-space:nowrap}
.art{background:linear-gradient(160deg,var(--art),#e7e0e0);border-radius:2px}

/* brand block */
.brand{position:absolute;left:12px;top:18px;width:150px;height:112px}
.brand .art{position:absolute;left:4px;top:0;width:34px;height:100px}
.brand .wordmark{position:absolute;left:44px;top:38px;font-size:14px;line-height:17px;white-space:normal;width:104px}
.brand .tagline{position:absolute;left:44px;top:92px;font-size:6px;color:var(--ink-soft);letter-spacing:.4px}

/* business cards */
.card{left:12px;width:150px;height:43px}
.card-front{top:137px}
.card-back{top:192px}
.card .art{position:absolute;left:6px;top:6px;width:12px;height:30px}
.card-front .wordmark{position:absolute;left:22px;top:18px;font-size:6px}
.card .contact{position:absolute;left:82px;top:6px;font-size:3.6px;line-height:5px;color:var(--ink)}
.card .contact b{color:var(--accent)}
.card .edge{position:absolute;right:0;top:0;width:5px;height:100%;background:var(--accent)}
.card-back .pattern{position:absolute;inset:0 5px 0 0;background:linear-gradient(135deg,var(--art-faint),#f8eeee 60%,var(--art-faint))}
.card-back .wordmark{position:absolute;left:28px;top:19px;font-size:6px}

/* letterheads */
.letterhead{top:19px;width:221px;height:293px}
.lh-1{left:163px}
.lh-2{left:403px}
.letterhead .art{position:absolute;left:2px;top:4px;width:13px;height:34px}
.letterhead .wordmark{position:absolute;left:20px;top:16px;font-size:6px}
.letterhead .contact{position:absolute;right:10px;top:8px;font-size:3.4px;line-height:5px;text-align:left}
.letterhead .watermark{position:absolute;left:80px;top:100px;width:64px;height:150px;background:linear-gradient(160deg,var(--art-faint),#f6f3f3);border-radius:3px}
.letterhead .footer{position:absolute;bottom:8px;width:100%;text-align:center;font-size:3.4px;line-height:5px;color:var(--ink-soft)}

/* flat envelopes */
.envelope{left:638px;width:250px;height:100px}
.env-1{top:67px}
.env-2{top:206px}
.envelope .art{position:absolute;left:6px;top:6px;width:10px;height:26px}
.envelope .wordmark{position:absolute;left:20px;top:14px;font-size:5px}
.envelope .return{position:absolute;left:20px;top:22px;font-size:3.2px;line-height:4px;color:var(--ink-soft)}

/* envelope set */
.env-set{position:absolute;left:900px;width:264px;box-shadow:var(--shadow)}
.env-set svg{display:block}
.set-black{top:60px;height:72px;z-index:1}
.set-red{top:108px;height:72px;z-index:2}
.set-white{top:199px;height:100px;z-index:1}
.env-set .mark{position:absolute;left:126px;width:12px;height:30px}
.set-black .mark{top:8px}
.set-white .mark{top:20px}
.set-caption{position:absolute;left:900px;top:305px;width:264px;font-size:5px;color:var(--ink-soft);text-align:center}
</style>
</head>
<body>

<section class="brand">
  <div class="art" role="img" aria-label="Illustration of a standing figure holding a red flower"></div>
  <div class="wordmark">Velvet Rooms LLC</div>
  <div class="tagline">Home Interiors</div>
</section>

<article class="item card card-front">
  <div class="art" role="img" aria-label="Small figure illustration with red flower"></div>
  <div class="wordmark">Velvet Rooms</div>
  <div class="contact"><b>Linnea Parcot Weller</b><br>Design Consultant<br>412 Quillon Lane<br>Palm Beach Gardens, FL 33587<br>LinneaParcot@velmorra.example<br>VelvetRooms.example</div>
  <div class="edge"></div>
</article>
<article class="item card card-back">
  <div class="pattern" role="img" aria-label="Scattered small red flower pattern"></div>
  <div class="wordmark">Velvet Rooms</div>
  <div class="edge"></div>
  <div class="caption">Business cards</div>
</article>

<article class="item letterhead lh-1">
  <div class="art" role="img" aria-label="Small figure illustration with red flower"></div>
  <div class="wordmark">Velvet Rooms</div>
  <div class="contact">412 Quillon Lane<br>Palm Beach Gardens, FL 33587<br>VelvetRooms.example</div>
  <div class="watermark" role="img" aria-label="Faint large figure illustration holding a flower"></div>
  <div class="footer">Linnea Parcot Weller · Design Consultant<br>LinneaParcot@velmorra.example</div>
  <div class="caption">Letterhead front</div>
</article>
<article class="item letterhead lh-2">
  <div class="watermark" role="img" aria-label="Faint large figure illustration holding a flower"></div>
  <div class="footer">412 Quillon Lane · Palm Beach Gardens, FL 33587<br>VelvetRooms.example</div>
  <div class="caption">Letterhead back</div>
</article>

<article class="item envelope env-1">
  <div class="art" role="img" aria-label="Small figure illustration with red flower"></div>
  <div class="wordmark">Velvet Rooms</div>
  <div class="return">412 Quillon Lane<br>Palm Beach Gardens, FL 33587</div>
  <div class="caption">Envelope front</div>
</article>
<article class="item envelope env-2">
  <div class="art" role="img" aria-label="Small figure illustration with red flower"></div>
  <div class="wordmark">Velvet Rooms</div>
  <div class="return">412 Quillon Lane<br>Palm Beach Gardens, FL 33587</div>
  <div class="caption">Envelope back</div>
</article>

<div class="env-set set-black">
  <svg width="264" height="72" viewBox="0 0 264 72">
    <rect width="264" height="72" fill="#2a2a2a"/>
    <path d="M0 0 L132 44 L264 0 Z" fill="#111"/>
  </svg>
  <div class="mark art" role="img" aria-label="Small figure illustration in white"></div>
</div>
<div class="env-set set-red">
  <svg width="264" height="72" viewBox="0 0 264 72">
    <rect width="264" height="72" fill="#f2f2f2"/>
    <path d="M0 0 L132 38 L264 0 Z" fill="#c8102e"/>
    <path d="M0 72 L132 32 L264 72" fill="none" stroke="#ddd" stroke-width="1"/>
  </svg>
</div>
<div class="env-set set-white">
  <svg width="264" height="100" viewBox="0 0 264 100">
    <rect width="264" height="100" fill="#fafafa"/>
    <path d="M0 0 L132 46 L264 0 Z" fill="#efefef" stroke="#ddd" stroke-width="1"/>
    <path d="M0 100 L132 44 L264 100" fill="none" stroke="#e2e2e2" stroke-width="1"/>
  </svg>
  <div class="mark art" role="img" aria-label="Small figure illustration with red flower"></div>
</div>
<div class="set-caption">Envelope set</div>

</body>
</html>
```